Military training company needs a Powerpoint desk template.

We need a Powerpoint deck that we can use for sales and training purposes. We are a training company for military mountaineering, so need something simple, clean and uncluttered that incorporates our logo and includes a placeholder for our tagline (under development). The colors need to complement and/or include the colors in the logo that was designed by Brightloom (attached below)

Requirements
Must have
• We need a title slide, table of content, etc. Please use the fonts and colors in the logo.

```html
<!DOCTYPE html>
<html lang="en">
<head>
<meta charset="utf-8">
<title>Altivane – Presentation Template</title>
<link href="https://fonts.googleapis.com/css2?family=Oswald:wght@500;600;700&family=Roboto:wght@400;500&family=Lato:wght@400;700&display=swap" rel="stylesheet">
<style>
  :root{
    --navy:#1c2541;
    --navy-deep:#151c33;
    --navy-photo:#233158;
    --tan:#a08868;
    --tan-dark:#8b7353;
    --cream:#e8e4cc;
    --cream-soft:#ece9d8;
    --ink:#222222;
    --page:#efefef;
    --white:#ffffff;
  }
  *{box-sizing:border-box;margin:0;padding:0}
  html,body{width:1200px;height:4152px;overflow:hidden;background:var(--page)}
  body{position:relative;font-family:"Lato",sans-serif;color:var(--ink)}

  .slide{position:absolute;width:680px;height:383px;transform:scale(1.613);transform-origin:0 0;
    overflow:hidden;background:var(--white);box-shadow:0 1px 3px rgba(0,0,0,.12)}
  .slide > svg.art{position:absolute;inset:0;width:680px;height:383px}
  .abs{position:absolute}

  /* corner badge */
  .badge-name{position:absolute;left:560px;top:30px;width:95px;text-align:center;
    font-family:"Oswald",sans-serif;font-weight:600;font-size:13px;letter-spacing:1.6px;color:var(--cream)}

  /* section heading */
  .heading{position:absolute;left:40px;top:27px;font-family:"Oswald",sans-serif;font-weight:600;
    font-size:24px;color:var(--tan);letter-spacing:.3px;line-height:1}

  /* cover + closing */
  .brand-name{position:absolute;left:0;width:680px;text-align:center;font-family:"Oswald",sans-serif;
    font-weight:700;font-size:46px;letter-spacing:7px;color:var(--cream);line-height:1}
  .tagline{position:absolute;left:0;width:680px;text-align:center;top:292px;font-family:"Oswald",sans-serif;
    font-weight:600;font-size:18.5px;color:var(--cream);letter-spacing:.2px}
  .thanks{position:absolute;left:0;width:680px;text-align:center;top:293px;font-family:"Oswald",sans-serif;
    font-weight:600;font-size:18px;color:var(--cream)}

  /* agenda */
  .agenda-title{position:absolute;left:330px;width:140px;text-align:center;top:56px;font-family:"Oswald",sans-serif;
    font-weight:600;font-size:22px;color:var(--tan)}
  .agenda-item{position:absolute;display:flex;align-items:center;gap:10px;font-family:"Roboto",sans-serif;
    font-size:17px;color:var(--ink)}
  .agenda-num{width:24px;height:24px;border-radius:50%;background:var(--navy);color:var(--white);
    font-size:11px;font-weight:500;display:flex;align-items:center;justify-content:center}

  /* about */
  .about-copy{position:absolute;left:33px;top:80px;width:281px;font-size:10.3px;line-height:21.4px;text-align:justify}
  .about-copy p + p{margin-top:12px}

  /* chart */
  .chart-label{position:absolute;width:80px;margin-left:-40px;text-align:center;font-family:"Oswald",sans-serif;line-height:1}
  .chart-label .name{display:block;font-size:7.5px;font-weight:500;letter-spacing:.2px}
  .chart-label .value{display:block;font-size:13px;font-weight:600;margin-top:7px}
  .is-tan{color:var(--tan)}
  .is-navy{color:var(--navy)}
  .chart-caption{position:absolute;left:90px;width:500px;top:306px;text-align:center;font-size:9.6px;line-height:17.5px;color:var(--navy)}

  /* team */
  .member{position:absolute;top:0;width:132px;height:383px;margin-left:-66px}
  .member-card{position:absolute;left:1px;top:250px;width:130px;height:74px;background:var(--white);
    box-shadow:0 1px 3px rgba(0,0,0,.18);border-bottom:3px solid var(--tan);text-align:center;padding:10px 5px 0}
  .member-card.navy{border-bottom-color:var(--navy)}
  .member-name{font-size:7.4px;font-weight:700;color:var(--tan);letter-spacing:.1px}
  .member-card.navy .member-name{color:var(--navy)}
  .member-role{font-size:5.2px;color:#555;margin-top:4px}
  .member-bio{font-size:4.6px;line-height:8px;color:#666;margin-top:4px}
</style>
</head>
<body>

<!-- Cover -->
<section class="slide" style="left:52px;top:58px">
  <svg class="art" viewBox="0 0 680 383" role="img" aria-label="Photo of soldiers standing in silhouette before snowy mountains, navy toned">
    <defs>
      <linearGradient id="coverPhoto" x1="0" y1="0" x2="0" y2="1">
        <stop offset="0" stop-color="#2a3a66"/>
        <stop offset=".55" stop-color="#22325a"/>
        <stop offset="1" stop-color="#1a2646"/>
      </linearGradient>
    </defs>
    <rect width="680" height="383" fill="url(#coverPhoto)"/>
  </svg>
  <div class="brand-name" style="top:127px">ALTIVANE</div>
  <div class="tagline">BRAVERY IS BEING THE ONLY ONE WHO KNOWS YOU’RE AFRAID</div>
</section>

<!-- Agenda -->
<section class="slide" style="left:56px;top:732px">
  <svg class="art" viewBox="0 0 680 383">
    <rect width="680" height="383" fill="#f4f4f4"/>
    <polygon points="0,0 345,0 65,383 0,383" fill="#d9d3b6" role="img" aria-label="Photo of two soldiers laughing at a laptop, cream toned"/>
    <polygon points="680,12 680,383 455,383" fill="#9b7f5c" role="img" aria-label="Photo of a soldier silhouette with rifle at sunset, brown toned"/>
    <polygon points="535,0 680,0 600,110" fill="var(--navy)"/>
  </svg>
  <div class="badge-name">ALTIVANE</div>
  <div class="agenda-title">AGENDA</div>
  <div class="agenda-item" style="left:341px;top:105px"><span class="agenda-num">01</span>Introduction</div>
  <div class="agenda-item" style="left:314px;top:160px"><span class="agenda-num">02</span>Section Slides</div>
  <div class="agenda-item" style="left:285px;top:215px"><span class="agenda-num">03</span>Our Team</div>
  <div class="agenda-item" style="left:257px;top:267px"><span class="agenda-num">04</span>Our Chart</div>
  <div class="agenda-item" style="left:233px;top:323px"><span class="agenda-num">05</span>Contact Us</div>
</section>

<!-- About -->
<section class="slide" style="left:56px;top:1408px">
  <svg class="art" viewBox="0 0 680 383">
    <polygon points="0,25 32,42 0,60" fill="var(--tan)"/>
    <polygon points="0,268 0,383 120,383" fill="var(--cream-soft)"/>
    <defs>
      <linearGradient id="ropePhoto" x1="0" y1="0" x2="1" y2="1">
        <stop offset="0" stop-color="#6b6a66"/>
        <stop offset=".5" stop-color="#4e4236"/>
        <stop offset="1" stop-color="#2f2a24"/>
      </linearGradient>
    </defs>
    <polygon points="483,25 691,383 275,383" fill="url(#ropePhoto)" role="img" aria-label="Photo of a gloved hand clipping a carabiner to a climbing rope"/>
    <polygon points="535,0 680,0 600,110" fill="var(--navy)"/>
  </svg>
  <div class="badge-name">ALTIVANE</div>
  <div class="heading">ABOUT ALTIVANE</div>
  <div class="about-copy">
    <p>Lorem ipsum dolor sit amet, consectetur adipiscing elit, sed do eiusmod tempor incididunt ut labore et dolore magna aliqua. Ut enim ad minim veniam, quis nostrud exercitation ullamco laboris nisi ut aliquip ex ea commodo consequat. Duis aute irure dolor in reprehenderit in voluptate velit esse cillum dolore eu fugiat nulla pariatur.</p>
    <p>Excepteur sint occaecat cupidatat non proident, sunt in culpa qui officia deserunt mollit anim id est laborum.</p>
  </div>
</section>

<!-- Chart -->
<section class="slide" style="left:52px;top:2097px">
  <svg class="art" viewBox="0 0 680 383">
    <polygon points="0,25 32,42 0,60" fill="var(--tan)"/>
    <g fill="var(--tan)">
      <polygon points="130,200 182,285 78,285"/>
      <polygon points="294,125 356,285 236,285"/>
      <polygon points="458,84 540,285 380,285"/>
    </g>
    <g fill="var(--navy)">
      <polygon points="201,170 269,285 133,285"/>
      <polygon points="361,186 419,285 303,285"/>
      <polygon points="524,150 602,285 447,285"/>
    </g>
    <polygon points="535,0 680,0 600,110" fill="var(--navy)"/>
  </svg>
  <div class="badge-name">ALTIVANE</div>
  <div class="heading">OUR CHART</div>
  <div class="chart-label is-tan" style="left:131px;top:156px"><span class="name">VOLUPTATEM</span><span class="value">10%</span></div>
  <div class="chart-label is-navy" style="left:201px;top:127px"><span class="name">CUPIDATAT</span><span class="value">30%</span></div>
  <div class="chart-label is-tan" style="left:294px;top:84px"><span class="name">OCCAECA</span><span class="value">50%</span></div>
  <div class="chart-label is-navy" style="left:363px;top:143px"><span class="name">EROCCAECA</span><span class="value">20%</span></div>
  <div class="chart-label is-tan" style="left:458px;top:42px"><span class="name">ROCCAECA</span><span class="value">90%</span></div>
  <div class="chart-label is-navy" style="left:527px;top:107px"><span class="name">KOCCAECA</span><span class="value">80%</span></div>
  <div class="chart-caption">Duis aute irure dolor in reprehenderit in voluptate velit esse cillum dolore eu fugiat nulla pariatur.<br>Excepteur sint occaecat cupidatat non proident, sunt in culpa qui officia<br>deserunt mollit anim id est laborum.</div>
</section>

<!-- Team -->
<section class="slide" style="left:56px;top:2781px">
  <svg class="art" viewBox="0 0 680 383">
    <polygon points="0,25 32,42 0,60" fill="var(--tan)"/>
    <polygon points="535,0 680,0 600,110" fill="var(--navy)"/>
    <defs>
      <linearGradient id="portrait" x1="0" y1="0" x2="0" y2="1">
        <stop offset="0" stop-color="#8a8580"/>
        <stop offset="1" stop-color="#3d3a38"/>
      </linearGradient>
    </defs>
    <g>
      <circle cx="99" cy="140" r="43" fill="var(--tan)"/>
      <circle cx="99" cy="140" r="40" fill="url(#portrait)" role="img" aria-label="Portrait photo of team member"/>
      <path d="M52,162 A47,47 0 0 0 146,162" fill="none" stroke="var(--tan)" stroke-width="3"/>
      <line x1="99" y1="190" x2="99" y2="247" stroke="#bbb" stroke-width=".6"/>
      <circle cx="99" cy="247" r="2.4" fill="var(--white)" stroke="var(--tan)" stroke-width="1"/>
    </g>
    <g>
      <circle cx="248" cy="140" r="43" fill="var(--navy)"/>
      <circle cx="248" cy="140" r="40" fill="url(#portrait)" role="img" aria-label="Portrait photo of team member at a laptop"/>
      <path d="M201,162 A47,47 0 0 0 295,162" fill="none" stroke="var(--navy)" stroke-width="3"/>
      <line x1="248" y1="190" x2="248" y2="247" stroke="#bbb" stroke-width=".6"/>
      <circle cx="248" cy="247" r="2.4" fill="var(--white)" stroke="var(--navy)" stroke-width="1"/>
    </g>
    <g>
      <circle cx="396" cy="140" r="43" fill="var(--tan)"/>
      <circle cx="396" cy="140" r="40" fill="url(#portrait)" role="img" aria-label="Portrait photo of team member"/>
      <path d="M349,162 A47,47 0 0 0 443,162" fill="none" stroke="var(--tan)" stroke-width="3"/>
      <line x1="396" y1="190" x2="396" y2="247" stroke="#bbb" stroke-width=".6"/>
      <circle cx="396" cy="247" r="2.4" fill="var(--white)" stroke="var(--tan)" stroke-width="1"/>
    </g>
    <g>
      <circle cx="545" cy="140" r="43" fill="var(--navy)"/>
      <circle cx="545" cy="140" r="40" fill="url(#portrait)" role="img" aria-label="Portrait photo of team member in an office"/>
      <path d="M498,162 A47,47 0 0 0 592,162" fill="none" stroke="var(--navy)" stroke-width="3"/>
      <line x1="545" y1="190" x2="545" y2="247" stroke="#bbb" stroke-width=".6"/>
      <circle cx="545" cy="247" r="2.4" fill="var(--white)" stroke="var(--navy)" stroke-width="1"/>
    </g>
  </svg>
  <div class="badge-name">ALTIVANE</div>
  <div class="heading">OUR TEAM</div>
  <div class="member" style="left:99px"><div class="member-card">
    <div class="member-name">DANIEL MARSH</div>
    <div class="member-role">Project Leader, Strategic Planning, Analysis</div>
    <div class="member-bio">Excepteur sint occaecat cupidatat non proident, sunt in culpa qui officia deserunt mollit anim id est laborum.</div>
  </div></div>
  <div class="member" style="left:248px"><div class="member-card navy">
    <div class="member-name">OWEN HARLOW</div>
    <div class="member-role">Project Manager Strategic Planning, Stakeholder</div>
    <div class="member-bio">Incididunt ut labore et dolore magna aliqua. Ut enim ad minim veniam, quis nostrud exercitation ullamco laboris nisi ut aliquip ex ea commodo</div>
  </div></div>
  <div class="member" style="left:396px"><div class="member-card">
    <div class="member-name">PETER VANCE</div>
    <div class="member-role">Economic Analysis, Investment Attraction</div>
    <div class="member-bio">Quis autem vel eum iure reprehenderit qui in ea voluptate velit esse quam nihil molestiae consequatur, vel illum</div>
  </div></div>
  <div class="member" style="left:545px"><div class="member-card navy">
    <div class="member-name">NORA ELLISON</div>
    <div class="member-role">Project Advisor</div>
    <div class="member-bio">Nemo enim ipsam voluptatem quia voluptas sit aspernatur aut odit aut fugit, sed quia consequuntur magni dolores eos qui</div>
  </div></div>
</section>

<!-- Closing -->
<section class="slide" style="left:56px;top:3460px">
  <svg class="art" viewBox="0 0 680 383" role="img" aria-label="Photo of a soldier on a misty ridge, navy toned">
    <defs>
      <linearGradient id="closePhoto" x1="0" y1="0" x2="1" y2="1">
        <stop offset="0" stop-color="#263760"/>
        <stop offset="1" stop-color="#1b2848"/>
      </linearGradient>
    </defs>
    <rect width="680" height="383" fill="url(#closePhoto)"/>
  </svg>
  <div class="brand-name" style="top:122px">ALTIVANE</div>
  <div class="thanks">THANK YOU</div>
</section>

</body>
</html>
```